Distribution/Printing company needs a web site to inform prospective customers on what we do.

Distribution/Printing/Packaging company needs a web site to inform prospective customers on what we do. Please look at our direct to consumer web site (under development) for an idea of the product lines we sell: storedev.thebrindlestock.com
Logo files are attached as is a flyer that is under development which contains other information about the company (this is to be used for content- not to be posted as is). The web site should be focused on our business customer base and is not intended to be direct to consumer. Site should have a link to our consumer web site.
Site design should be mobile friendly, or mobile could be redirected to a mobile version. This web site will be strictly informational and will not be designed for any sales transactions.

Target Market(s)

Manufacturing and retail businesses, any other multi-site business that would benefit from centralized pricing and budget controls we can provide (banks, medical/dental offices, educational facilities, etc).

Requirements
Must have
• 1) Top level menu: Products, about us, locations, contact us, news
• 2) page with news/promotions that is easily updated
• 3) "contact us" form (name, company, phone, email address) email link
• 4) link to www.store.thebrindlestock.com with information that lower pricing is available for businesses
• 5) SEO keywords
• 6) Link to powerpoint presentation file
Nice to have
• 1) our phone number should appear on every page near the top

```html
<!DOCTYPE html>
<html lang="en">
<head>
<meta charset="utf-8">
<title>Granite Row Supply — Packaging, Printing, Distribution</title>
<link href="https://fonts.googleapis.com/css2?family=Open+Sans:wght@400;600;700&family=Raleway:wght@600;700&display=swap" rel="stylesheet">
<style>
:root{
  --ink:#1f1d1e;
  --bar:#2a2829;
  --page:#f2f1f3;
  --card:#252324;
  --white:#ffffff;
  --muted:#8a8a8a;
  --footer:#2f2f2f;
  --footer-base:#262626;
  --rule:#2b2b2b;
  --btn:#555555;
}
*{box-sizing:border-box;margin:0;padding:0}
html,body{width:1200px;height:2961px;overflow:hidden}
body{background:var(--page);font-family:"Open Sans",Arial,sans-serif;color:var(--ink);position:relative}
.abs{position:absolute}

/* top bar */
.topbar{left:0;top:0;width:1200px;height:36px;background:var(--bar);color:var(--white);font-size:12px;font-weight:600}
.topbar .item{position:absolute;top:0;height:36px;display:flex;align-items:center;gap:8px;text-transform:uppercase}
.topbar svg{fill:var(--white)}
.search{position:absolute;left:937px;top:6px;width:164px;height:23px;background:var(--white);border-radius:3px;font-size:10px;color:#777;font-style:italic;padding:4px 8px}
.search svg{position:absolute;right:6px;top:5px;fill:#333}

/* header */
.brand{left:99px;top:52px;width:240px}
.brand-name{display:flex;align-items:center;gap:10px;font-weight:700;font-size:17px;letter-spacing:.3px;text-transform:uppercase;color:var(--ink)}
.brand-mark{width:14px;height:14px;background:var(--ink)}
.brand-tag{margin-top:4px;font-size:11.5px;font-weight:600;padding-left:24px}
.nav{left:448px;top:88px;display:flex;font-size:12.5px;font-weight:600;text-transform:uppercase}
.nav a{display:block;color:var(--ink);text-decoration:none;padding:8px 17px;margin-right:13px}
.nav a.active{border-top:1px solid var(--ink);border-bottom:3px solid var(--ink)}

/* hero */
.hero{left:0;top:172px;width:1200px;height:513px;background:linear-gradient(120deg,#bdb7ac 0%,#d9d6d1 35%,#9c9a9a 60%,#cfcac4 100%)}
.hero-arrow{top:374px;width:28px;height:108px;background:var(--bar);display:flex;align-items:center;justify-content:center}
.hero-arrow svg{fill:var(--white)}
.dots{left:549px;top:702px;display:flex;gap:9px}
.dots span{width:17px;height:17px;border-radius:50%;background:#8d8d8d}
.dots span.on{background:var(--ink)}

/* welcome */
.rule{left:99px;width:1002px;height:3px;background:var(--rule)}
.welcome{left:99px;top:776px;width:1002px;text-align:center}
.welcome h1{font-weight:400;font-size:37px;letter-spacing:.5px;text-transform:uppercase}
.welcome p{margin-top:14px;font-size:13px;line-height:20px;text-transform:uppercase;padding:0 30px}
.btn-more{display:inline-block;margin-top:27px;width:112px;height:39px;line-height:39px;background:var(--ink);color:var(--white);font-size:12px;font-weight:600;text-transform:uppercase}

/* features */
.feature{top:1020px;width:321px;height:375px;background:var(--card);color:var(--white);text-align:center}
.feature svg{position:absolute;left:50%;top:52px;transform:translateX(-50%);fill:var(--white)}
.feature h2{position:absolute;left:0;right:0;top:166px;font-family:"Raleway",Arial,sans-serif;font-weight:700;font-size:38px}
.feature p{position:absolute;left:30px;right:30px;top:216px;font-size:15px;line-height:24px}

/* newsletter */
.newsletter{left:0;top:1460px;width:1200px;height:415px;background:linear-gradient(115deg,#3a3b6a 0%,#2b2d55 30%,#4a4376 55%,#2d2f50 80%,#403f6d 100%)}
.nl-icon{left:312px;top:1609px;fill:var(--white)}
.nl-text{left:389px;top:1612px;width:520px;color:var(--white);font-size:19px;line-height:26px;text-transform:uppercase}
.nl-input{left:312px;top:1672px;width:355px;height:49px;background:var(--white);font-size:14px;font-style:italic;color:#bbb;padding:15px 14px}
.nl-submit{left:677px;top:1672px;width:174px;height:49px;background:var(--btn);color:var(--white);font-size:20px;text-align:center;line-height:49px}

/* promo */
.promo-box{left:99px;top:1936px;width:489px;height:448px;background:var(--card);color:var(--white);text-align:center}
.promo-box h2{position:absolute;left:20px;right:20px;top:38px;font-family:"Raleway",Arial,sans-serif;font-weight:600;font-size:49px;line-height:58px}
.promo-box p{position:absolute;left:40px;right:40px;top:290px;font-size:15px;line-height:24px}
.promo-photo{left:612px;top:1936px;width:489px;height:448px;background:linear-gradient(135deg,#eef1f4 0%,#dfe3e8 40%,#c9b8a6 70%,#e7e9ec 100%)}

/* footer */
.footer{left:0;top:2428px;width:1200px;height:458px;background:var(--footer)}
.f-col{top:2457px;width:240px}
.f-col h3{font-family:"Raleway",Arial,sans-serif;font-weight:700;font-size:27px;color:var(--white);margin-bottom:14px}
.f-col li{list-style:none;font-size:13px;color:var(--muted);height:35px}
.map{left:612px;top:2457px;width:489px;height:397px;background:linear-gradient(145deg,#3a3d44 0%,#2c2f36 50%,#34373e 100%)}
.base{left:0;top:2886px;width:1200px;height:75px;background:var(--footer-base);color:var(--muted);font-size:12px;text-align:center;line-height:75px}
</style>
</head>
<body>

<div class="abs topbar">
  <div class="item" style="left:99px">
    <svg width="11" height="15" viewBox="0 0 12 16"><path d="M6 0a6 6 0 0 0-6 6c0 4.5 6 10 6 10s6-5.5 6-10a6 6 0 0 0-6-6zm0 8.5A2.5 2.5 0 1 1 6 3.5a2.5 2.5 0 0 1 0 5z"/></svg>
    1290 Larkfield Road, Glasgow DX4 72KP
  </div>
  <div class="item" style="left:437px">
    <svg width="14" height="14" viewBox="0 0 16 16"><path d="M3.5 1l2.5 3-1.5 2c1 2 3 4 5 5l2-1.5 3 2.5-1.5 3C7 14.5 1.5 9 1 2.5z"/></svg>
    800-5512-3047
  </div>
  <div class="item" style="left:589px">
    <svg width="17" height="12" viewBox="0 0 18 12"><path d="M0 0h18v12H0zM1.5 1.5v.4L9 7l7.5-5.1v-.4zm0 2.2v6.8h15V3.7L9 8.8z"/></svg>
    info@graniterowsupply.net
  </div>
  <div class="search">Search
    <svg width="12" height="12" viewBox="0 0 12 12"><path d="M5 0a5 5 0 0 1 4 8l3 3-1 1-3-3a5 5 0 1 1-3-9zm0 1.5a3.5 3.5 0 1 0 0 7 3.5 3.5 0 0 0 0-7z"/></svg>
  </div>
</div>

<div class="abs brand">
  <div class="brand-name"><span class="brand-mark"></span>Granite Row Supply</div>
  <div class="brand-tag">Packaging • Printing • Distribution</div>
</div>

<nav class="abs nav">
  <a class="active" href="#">Home</a>
  <a href="#">About us</a>
  <a href="#">Products</a>
  <a href="#">News</a>
  <a href="#">Locations</a>
  <a href="#">Contact us</a>
</nav>

<div class="abs hero" role="img" aria-label="Photo of a hand with a pen pressing keys on a calculator beside coins and financial charts"></div>
<div class="abs hero-arrow" style="left:0"><svg width="10" height="14" viewBox="0 0 10 14"><path d="M8 0l2 2-5 5 5 5-2 2-7-7z"/></svg></div>
<div class="abs hero-arrow" style="left:1172px"><svg width="10" height="14" viewBox="0 0 10 14"><path d="M2 0L0 2l5 5-5 5 2 2 7-7z"/></svg></div>
<div class="abs dots"><span></span><span class="on"></span><span></span><span></span></div>

<div class="abs rule" style="top:738px"></div>
<section class="abs welcome">
  <h1>Welcome to our website</h1>
  <p>Our company is one of the leading recycling, renewable energy and waste management companies. We work with more than 90 local authorities and thousands of private customers across the country.</p>
  <span class="btn-more">More</span>
</section>
<div class="abs rule" style="top:971px"></div>

<article class="abs feature" style="left:99px">
  <svg width="72" height="72" viewBox="0 0 72 72"><path d="M38 6a30 30 0 1 1-28 40l7-3a22.5 22.5 0 1 0 3-22l7 7H6V7l8 8A30 30 0 0 1 38 6z"/><path d="M34 22h6v16l10 8-4 5-12-10z"/></svg>
  <h2>Quick installs</h2>
  <p>Lorem ipsum dolor sit amet conse ctetur adipisicing elit, sed do eiusmod tempor incididunt ut labore.</p>
</article>
<article class="abs feature" style="left:440px">
  <svg width="72" height="72" viewBox="0 0 72 72"><path d="M36 4c2 0 3 1 3 3v2c16 2 29 14 31 30-3-4-7-6-11-6s-8 2-11 6c-2-4-5-6-9-6v24c0 6-4 10-10 10S19 63 19 57h6c0 3 2 5 4 5s4-2 4-5V33c-4 0-7 2-9 6-3-4-7-6-11-6S6 35 3 39C5 23 18 11 33 9V7c0-2 1-3 3-3z"/></svg>
  <h2>Support</h2>
  <p>Lorem ipsum dolor sit amet conse ctetur adipisicing elit, sed do eiusmod tempor incididunt ut labore.</p>
</article>
<article class="abs feature" style="left:782px">
  <svg width="86" height="78" viewBox="0 0 86 78"><path d="M24 20l5-1 2 7 5 2 6-4 4 4-4 6 2 5 7 2v6l-7 2-2 5 4 6-4 4-6-4-5 2-2 7h-6l-2-7-5-2-6 4-4-4 4-6-2-5-7-2v-6l7-2 2-5-4-6 4-4 6 4 5-2 2-7zm3 17a9 9 0 1 0 0 18 9 9 0 0 0 0-18z"/><path d="M62 0h5l1 5 4 2 4-3 4 4-3 4 2 4 5 1v5l-5 1-2 4 3 4-4 4-4-3-4 2-1 5h-5l-1-5-4-2-4 3-4-4 3-4-2-4-5-1v-5l5-1 2-4-3-4 4-4 4 3 4-2zm2.5 12a5 5 0 1 0 0 10 5 5 0 0 0 0-10z"/><path d="M64 42h4l1 4 3 1 3-2 3 3-2 3 1 3 4 1v4l-4 1-1 3 2 3-3 3-3-2-3 1-1 4h-4l-1-4-3-1-3 2-3-3 2-3-1-3-4-1v-4l4-1 1-3-2-3 3-3 3 2 3-1zm2 10a4 4 0 1 0 0 8 4 4 0 0 0 0-8z"/></svg>
  <h2>Customizable</h2>
  <p>Lorem ipsum dolor sit amet conse ctetur adipisicing elit, sed do eiusmod tempor incididunt ut labore.</p>
</article>

<section class="abs newsletter" role="img" aria-label="Photo of a night city skyline with light trails in violet and blue tones"></section>
<svg class="abs nl-icon" width="56" height="43" viewBox="0 0 56 43"><path d="M0 0h56v43H0zm4 4v3l24 16 24-16V4zm0 8v27h48V12L28 28z"/></svg>
<div class="abs nl-text">Subscribe to our newsletter to receive news, updates, and another stuff by email.</div>
<div class="abs nl-input">Email</div>
<div class="abs nl-submit">Submit</div>

<section class="abs promo-box">
  <h2>Let us make a difference in your web design</h2>
  <p>Lorem ipsum dolor sit amet conse ctetur adipisicing elit, sed do eiusmod tempor incididunt ut labore et dolore magna aliqua. Ut enim ad minim veniam.</p>
</section>
<div class="abs promo-photo" role="img" aria-label="Photo of two colleagues smiling while looking at a laptop"></div>

<footer class="abs footer"></footer>
<div class="abs f-col" style="left:99px">
  <h3>About</h3>
  <ul>
    <li>Lorem ipsum dolor sit amet</li>
    <li>Conse ctetur adipisicing</li>
    <li>Elit sed do eiusmod tempor</li>
    <li>Incididunt ut labore</li>
    <li>Et dolore magna aliqua</li>
    <li>Ut enim ad minim veniam</li>
    <li>Quis nostrud exercitat</li>
  </ul>
</div>
<div class="abs f-col" style="left:355px">
  <h3>Services</h3>
  <ul>
    <li>Conse ctetur adipisicing</li>
    <li>Elit sed do eiusmod tempor</li>
    <li>Incididunt ut labore</li>
    <li>Et dolore magna aliqua</li>
    <li>Ut enim ad minim veniam</li>
    <li>Quis nostrud exercitat</li>
  </ul>
</div>
<div class="abs map" role="img" aria-label="Dark street map showing the company location with a red pin"></div>
<div class="abs base">Copyright © 2015 Granite Row Supply - All Rights Reserved</div>

</body>
</html>
```